Attorney business card for two offices

Looking for a new business card design that can list both of my offices, one in Houston and one in West Texas. Want something masculine, easy to read, and conservative yet somewhat modern. Our current card has used a nautical star on it for years, but I am not necessarily attached to that. Also, a lot of our forms use dark green and orange. Second office address is P.O. Box 518, Marathon, Texas 79617

```html
<!DOCTYPE html>
<html lang="en">
<head>
<meta charset="utf-8">
<title>Garner Law Firm – Business Card</title>
<link rel="stylesheet" href="https://fonts.googleapis.com/css2?family=Cinzel:wght@400&family=Montserrat:wght@400&family=Arimo:wght@400&display=swap">
<style>
  :root{
    --backdrop:#2b2b2d;
    --card:#1c1d1f;
    --green:#1f7c12;
    --orange:#d99a1e;
    --ink:#f2f2f2;
    --rule:#5a5a5c;
    --icon-ink:#0d2a08;
  }
  *{margin:0;padding:0;box-sizing:border-box}
  html,body{width:1200px;height:1108px;overflow:hidden;background:var(--backdrop)}
  .stage{width:1200px;height:1108px;display:flex;justify-content:center;align-items:center;gap:80px}
  .card{position:relative;width:420px;height:700px;background:var(--card);border-radius:18px;box-shadow:0 18px 40px rgba(0,0,0,.45);overflow:hidden;text-align:center}

  .firm-name{font-family:"Arimo",sans-serif;font-weight:400;color:var(--green);font-size:24px;line-height:1.2;letter-spacing:.3px}

  .front .firm-name{margin-top:170px}
  .attorney{margin-top:50px}
  .attorney-name{font-family:"Cinzel",serif;font-size:30px;color:var(--green);line-height:1.1}
  .attorney-title{font-family:"Montserrat",sans-serif;font-size:15px;color:var(--orange);margin-top:4px;letter-spacing:.5px}

  .icon-row{display:flex;align-items:center;justify-content:center;gap:6px;margin:16px 0 14px}
  .icon-row::before,.icon-row::after{content:"";flex:0 0 48px;height:1px;background:var(--rule);margin:0 8px}
  .icon{width:30px;height:30px;border-radius:5px;background:var(--green);display:flex;align-items:center;justify-content:center}
  .icon svg{width:18px;height:18px;fill:none;stroke:var(--icon-ink);stroke-width:2;stroke-linecap:round;stroke-linejoin:round}

  .contact,.address{font-family:"Arimo",sans-serif;color:var(--ink);font-size:19px;line-height:1.32}

  .pin-row{margin:14px 0 12px}
  .pin-row .icon{width:28px;height:34px}
  .pin-row::before,.pin-row::after{flex-basis:100px}

  .back .pattern{position:absolute;inset:0 0 210px 0;background:linear-gradient(180deg,#38393c 0%,#2a2b2e 45%,#1c1d1f 100%)}
  .back .firm-name{position:absolute;left:0;right:0;bottom:100px}
</style>
</head>
<body>
<main class="stage">

  <section class="card front">
    <div class="firm-name">The Garner Law Firm P.C.</div>

    <div class="attorney">
      <div class="attorney-name">Daniel R. Garner, Sr.</div>
      <div class="attorney-title">ATTORNEY AT LAW</div>
    </div>

    <div class="icon-row">
      <span class="icon" aria-label="Phone"><svg viewBox="0 0 24 24"><path d="M5 4h4l2 5-3 2a11 11 0 0 0 5 5l2-3 5 2v4a2 2 0 0 1-2 2A17 17 0 0 1 3 6a2 2 0 0 1 2-2z"/></svg></span>
      <span class="icon" aria-label="Fax"><svg viewBox="0 0 24 24"><path d="M6 9V3h12v6"/><rect x="3" y="9" width="18" height="8" rx="2"/><path d="M6 14h12v7H6z"/></svg></span>
      <span class="icon" aria-label="Email"><svg viewBox="0 0 24 24"><rect x="3" y="5" width="18" height="14" rx="1"/><path d="M3 6l9 7 9-7"/></svg></span>
      <span class="icon" aria-label="Website"><svg viewBox="0 0 24 24"><circle cx="12" cy="12" r="9"/><path d="M3 12h18M12 3a14 14 0 0 1 0 18M12 3a14 14 0 0 0 0 18"/></svg></span>
    </div>

    <div class="contact">
      (713) 555-0142<br>
      (832) 555-0176<br>
      daniel@garnertxlaw.com<br>
      www.garnertxlaw.com
    </div>

    <div class="icon-row pin-row">
      <span class="icon" aria-label="Address"><svg viewBox="0 0 24 24"><path d="M12 21s-6-6-6-11a6 6 0 0 1 12 0c0 5-6 11-6 11z"/><circle cx="12" cy="10" r="2"/></svg></span>
    </div>

    <div class="address">
      4810 Prairie Oak Drive, Suite 210<br>
      Houston, Texas 77055<br>
      P.O. Box 518, Marathon<br>
      Texas 79617
    </div>
  </section>

  <section class="card back">
    <div class="pattern" role="img" aria-label="Decorative scattered pattern fading from grey to black"></div>
    <div class="firm-name">The Garner Law Firm P.C.</div>
  </section>

</main>
</body>
</html>
```